Aloft Aviatrix Pilot

I am looking for a personal business card, for a very well qualified female pilot, with a lot of aviation experience.

Currently an airline pilot, have worked as a bush pilot in Africa, looking to get into corporate aviation, or private jet owners.
Want a classy looking card for networking...

Could be interested in a retro\vintage look also?!

An idea,, is an african sunset background, with my wings\logo on it
Updates

I just want to say thank you to all of your for your amazing designs!

I have been very busy flying this past week , so not had a chance to be on the computer much.
But I provide some feedback, and conclusions very soon!
Thank you again.

Marla

Reason: Still waiting on a couple of revisions to be 100% about my choice!

Target Market(s)

corporate aviation, private jet owners, casino's,
General audience.
networking

Industry/Entity Type

Airline

Requirements
Nice to have
• Classy, edgy, sexy, but also feminine

```html
<!DOCTYPE html>
<html lang="en">
<head>
<meta charset="utf-8">
<title>Pilot Business Card</title>
<link rel="stylesheet" href="https://fonts.googleapis.com/css2?family=Poiret+One&family=PT+Sans:wght@400;700&display=swap">
<style>
  :root {
    --backdrop: #2b2320;
    --card-black: #1c1d1f;
    --card-black-edge: #0b0b0c;
    --card-white: #f1f1f1;
    --card-white-shade: #d4d4d4;
    --gold-light: #f3d98a;
    --gold: #c9a03a;
    --gold-dark: #7a5a14;
    --ink: #1a1a1a;
    --title: #ffffff;
  }
  * { box-sizing: border-box; margin: 0; padding: 0; }
  html, body { width: 1200px; height: 900px; overflow: hidden; }
  body {
    background: var(--backdrop);
    font-family: "PT Sans", sans-serif;
    position: relative;
  }
  .piece-title {
    position: absolute;
    top: 28px; right: 30px;
    font-family: "Poiret One", sans-serif;
    font-weight: 400;
    font-size: 52px;
    color: var(--title);
    letter-spacing: 0.5px;
  }
  .card {
    position: absolute;
    left: 250px;
    width: 640px;
    height: 366px;
    box-shadow: 0 18px 40px rgba(0,0,0,.55);
  }
  .card-front {
    top: 120px;
    background: radial-gradient(ellipse at 55% 40%, #3a3b3e 0%, var(--card-black) 55%, var(--card-black-edge) 100%);
  }
  .card-back {
    top: 510px;
    background: linear-gradient(160deg, var(--card-white) 0%, #ffffff 40%, var(--card-white-shade) 100%);
    text-align: center;
    color: var(--ink);
  }
  .stripe-group {
    position: absolute;
    top: 0; bottom: 0;
    width: 90px;
    display: flex;
    justify-content: space-between;
  }
  .stripe-group.left { left: 22px; }
  .stripe-group.right { right: 22px; }
  .stripe {
    width: 20px;
    height: 100%;
    background: linear-gradient(180deg, var(--gold-dark) 0%, var(--gold) 25%, var(--gold-light) 55%, var(--gold) 80%, var(--gold-dark) 100%);
  }
  .brand {
    display: flex;
    align-items: center;
    justify-content: center;
    gap: 12px;
    font-weight: 700;
    color: var(--gold);
    letter-spacing: 1px;
  }
  .brand-dot {
    width: 14px; height: 14px;
    border-radius: 50%;
    background: var(--gold);
  }
  .card-front .brand {
    position: absolute;
    top: 50%; left: 0; right: 0;
    transform: translateY(-50%);
    font-size: 34px;
  }
  .card-back .brand {
    margin-top: 46px;
    font-size: 30px;
  }
  .holder-name {
    margin-top: 64px;
    font-size: 22px;
    font-weight: 700;
  }
  .contact {
    margin-top: 26px;
    font-size: 17px;
    line-height: 1.35;
  }
  .address {
    margin-top: 22px;
    font-size: 17px;
  }
</style>
</head>
<body>
  <h1 class="piece-title">Aloft Aviatrix Pilot</h1>

  <section class="card card-front" aria-label="Card front">
    <div class="stripe-group left"><span class="stripe"></span><span class="stripe"></span><span class="stripe"></span></div>
    <div class="brand"><span class="brand-dot"></span>Aloft Aviatrix</div>
    <div class="stripe-group right"><span class="stripe"></span><span class="stripe"></span><span class="stripe"></span></div>
  </section>

  <section class="card card-back" aria-label="Card back">
    <div class="brand"><span class="brand-dot"></span>Aloft Aviatrix</div>
    <p class="holder-name">Capt. Fiona Marla</p>
    <p class="contact">1-555-010-2418<br>fionamarlacaptain@mail.com</p>
    <p class="address">1200 Harbor View Road, Seaside, CA 90000</p>
  </section>
</body>
</html>
```